依頼概要
■依頼の目的/概要
遊技業組合のポスターデザインの制作をお願いします。
パチンコ店の出玉を換金せずにお楽しみ袋と交換して家に持ち帰ってもらうよう呼びかけるポスターです。。
カウンター前にお楽しみ袋が積まれたワゴンを設置(添付PDF)
店内にポスターを貼ります。

■依頼詳細
過去の制作は26年1月はポスター。26年12月はPOPスタンドパネル。27年はのぼり、昨年28年12月はポスターを制作。
http://www.hanamizu-kumiai.jp/event/index.cgi

・パチンコ・スロットのホール内に掲示します。
・ホール内で目につくカラー・デザインをお願いします。
・社会を風刺作品や今年の流行をとり入れていただくなど。

■原稿内容
・カラー B2ポスター
・景品持ち帰り推進運動
・平成29年12月16日(土)~平成29年1月24日(日)
・山並遊興事業協同組合
コピーはお任せいたします。

その他何かご不明な点がございましたら、お気軽にご質問下さい。
よろしくお願いいたします。
■ 選んだ理由

大変お待たせしました。
どのデザインも好評でしたが目に留まることで選ばれました。
ありがとうございました。 森下

■ 提案者全員のお礼・コメント

たくさんの提案ありがとうございました。
ありがとうございました。 森下

```html
<!DOCTYPE html>
<html lang="ja">
<head>
<meta charset="utf-8">
<title>景品持ち帰り推進運動 ポスター</title>
<link rel="stylesheet" href="https://fonts.googleapis.com/css2?family=Noto+Sans+JP:wght@500;700;900&display=swap">
<style>
  :root {
    --green: #1d9a4b;
    --green-dark: #17703a;
    --red: #e1232b;
    --white: #ffffff;
    --gold: #f3a700;
    --tree-top: #ffffff;
    --tree-bottom: #dcefe2;
    --mascot-top: #ffffff;
    --mascot-bottom: #ececec;
    --ink: #1f1f1f;
    --ink-red: #d2232a;
  }
  html, body {
    margin: 0;
    padding: 0;
    width: 847px;
    height: 1200px;
    overflow: hidden;
  }
  .poster {
    position: relative;
    width: 847px;
    height: 1200px;
    overflow: hidden;
    font-family: "Noto Sans JP", sans-serif;
    background: var(--red);
  }
  .band-top {
    position: absolute;
    left: 0; top: 0;
    width: 847px; height: 600px;
    background: var(--green);
  }
  .band-bottom {
    position: absolute;
    left: 0; top: 600px;
    width: 847px; height: 600px;
    background: var(--red);
  }
  .headline {
    position: absolute;
    margin: 0;
    writing-mode: vertical-rl;
    color: var(--white);
    font-weight: 900;
    font-size: 128px;
    line-height: 1;
    letter-spacing: 4px;
  }
  .headline--family { left: 12px; top: 50px; }
  .headline--holy { left: 702px; top: 22px; }
  .headline--bag { left: 12px; top: 636px; }
  .headline--newyear { left: 702px; top: 636px; }

  .artwork-tree {
    position: absolute;
    left: 250px; top: 40px;
    width: 356px; height: 520px;
    border-radius: 12px;
    background: linear-gradient(180deg, var(--tree-top) 0%, var(--tree-bottom) 100%);
  }

  .sun-disc {
    position: absolute;
    left: 264px; top: 652px;
    width: 320px; height: 320px;
  }
  .sun-disc circle { fill: var(--gold); }

  .artwork-mascot {
    position: absolute;
    left: 300px; top: 700px;
    width: 248px; height: 460px;
    border-radius: 110px 110px 10px 10px;
    background: linear-gradient(180deg, var(--mascot-top) 0%, var(--mascot-bottom) 100%);
  }

  .campaign-tag {
    position: absolute;
    left: 258px; top: 548px;
    width: 326px; height: 130px;
    background: var(--white);
    transform: rotate(-5deg);
    box-shadow: 0 3px 0 rgba(0,0,0,0.15);
    text-align: center;
    color: var(--ink);
  }
  .campaign-title {
    margin: 16px 0 0;
    font-weight: 900;
    font-size: 32px;
    line-height: 1.12;
    color: var(--green-dark);
  }
  .campaign-dates {
    margin: 8px 0 0;
    font-weight: 900;
    font-size: 24px;
    line-height: 1.1;
    color: var(--ink);
  }
  .campaign-dates .day {
    display: inline-block;
    width: 26px; height: 26px;
    border-radius: 50%;
    background: var(--ink-red);
    color: var(--white);
    font-size: 15px;
    line-height: 26px;
    vertical-align: 2px;
  }

  .issuer {
    position: absolute;
    right: 18px; bottom: 12px;
    margin: 0;
    color: var(--white);
    font-weight: 500;
    font-size: 17px;
    letter-spacing: 1px;
  }
</style>
</head>
<body>
<main class="poster">
  <div class="band-top"></div>
  <div class="band-bottom"></div>

  <h1 class="headline headline--holy">聖夜も、</h1>
  <p class="headline headline--family">家族喜ぶ</p>
  <p class="headline headline--newyear">新年も、</p>
  <p class="headline headline--bag">景品袋。</p>

  <div class="artwork-tree" role="img" aria-label="星と赤いクリスマスブーツを飾った白いクリスマスツリーのイラスト"></div>

  <svg class="sun-disc" viewBox="0 0 320 320" aria-hidden="true">
    <circle cx="160" cy="160" r="160"/>
  </svg>

  <div class="artwork-mascot" role="img" aria-label="「福袋」と書かれた紅白の袋を抱えた白い犬のイラスト"></div>

  <div class="campaign-tag">
    <p class="campaign-title">景品持ち帰り<br>推進運動</p>
    <p class="campaign-dates">H29 12/16<span class="day">土</span>▶24<span class="day">日</span></p>
  </div>

  <p class="issuer">山並遊興事業協同組合</p>
</main>
</body>
</html>
```